Chip Shop app

This task requires the creation of a number of images/icons for an example Zorvex app to demonstrate functionality in a forthcoming product.
The app will be called 'Velto' for a made up Fish n' Chip shop . The app will demonstrate the ability to request a delivery of food. The app will also provide prices and the ability to check on the current status of delivery. Icons will be needed (discussed below).
The following images are required:
A 90 x 90 pixel button (png and 180x180 retina versions too) for each of the following:
- A 'Menu' icon
- A 'Prices' icon
- A 'Order' icon
- Two 320 x 480 pixels background images (png and 640 x 960 retina version).
One of these images will be used for the 'Splash' image shown to a user when the app loads. The other background image will be used for the main app page where the buttons will be shown.
The 3 buttons will occupy the main page so the background of the main page should fit nicely with whatever position the 3 buttons will be placed in.
- An app icon (57 x 57 pixels and an identical 114 x 114 pixel for retina)
- A Melodrin connection image (512 x 512 pixels and a 1024 x 1024 identical version).
Since this is a made up company, the design is a 'blank canvas', so to speak. We're looking for something that looks beautiful and will do our app justice when put on display in the Quillbay.

```html
<!DOCTYPE html>
<html lang="en">
<head>
<meta charset="utf-8">
<title>Velto – Delivery App Screens</title>
<link rel="stylesheet" href="https://fonts.googleapis.com/css2?family=Oswald:wght@400;600&display=swap">
<style>
  :root {
    --canvas-bg: #2b2725;
    --wordmark: #ffc24a;
    --tagline: #b3261a;
    --panel-grey: #4a4a4a;
    --panel-grey-dark: #2e2e2e;
    --divider: #8a8a8a;
    --button-glass: rgba(255, 255, 255, 0.42);
    --button-icon: #1e1e1e;
    --icon-tile: #f2f2f2;
    --icon-tile-edge: #d6d6d6;
    --fry-gold: #f6a91c;
    --fry-deep: #d8660f;
  }
  * { box-sizing: border-box; margin: 0; padding: 0; }
  html, body { width: 1200px; height: 788px; overflow: hidden; }
  body {
    position: relative;
    background: var(--canvas-bg);
    font-family: "Oswald", "Arial Narrow", sans-serif;
  }

  .screen {
    position: absolute;
    top: 203px;
    height: 389px;
    overflow: hidden;
  }

  /* Splash screen */
  .splash { left: 93px; width: 274px; }
  .splash-photo {
    position: absolute; inset: 0;
    background:
      radial-gradient(ellipse 70% 40% at 50% 30%, rgba(214, 120, 40, 0.55), transparent 70%),
      linear-gradient(180deg, #3a1d0e 0%, #8a4a1c 32%, #b0652a 48%, #6b5a58 70%, #3c3a40 100%);
  }
  .splash-brand {
    position: absolute; left: 0; right: 0; top: 152px;
    text-align: center;
  }
  .splash-name {
    display: block;
    font-weight: 400;
    font-size: 54px;
    line-height: 1;
    letter-spacing: 3px;
    color: var(--wordmark);
  }
  .splash-tagline {
    display: block;
    margin-top: 4px;
    font-weight: 600;
    font-size: 19px;
    letter-spacing: 1px;
    color: var(--tagline);
  }

  /* Main screen */
  .main { left: 478px; width: 277px; }
  .main-header {
    position: absolute; left: 0; top: 0; width: 100%; height: 185px;
    background: radial-gradient(ellipse at 50% 45%, var(--panel-grey) 0%, var(--panel-grey-dark) 100%);
    border-bottom: 2px solid var(--divider);
  }
  .header-emblem {
    position: absolute; left: 68px; top: 26px; width: 150px; height: 108px;
    border-radius: 50% 40% 40% 50% / 50%;
    background: radial-gradient(ellipse at 45% 50%, var(--fry-gold) 0%, var(--fry-deep) 75%, rgba(216, 102, 15, 0) 100%);
  }
  .main-photo {
    position: absolute; left: 0; top: 185px; width: 100%; height: 204px;
    background:
      radial-gradient(ellipse 80% 45% at 50% 55%, rgba(200, 120, 50, 0.75), transparent 75%),
      linear-gradient(180deg, #3a2a28 0%, #7a4e2a 35%, #8d7a90 70%, #2c2a30 100%);
  }
  .action-row {
    position: absolute; left: 17px; top: 245px;
    display: flex; gap: 13px;
  }
  .action-button {
    width: 72px; height: 71px;
    background: var(--button-glass);
    display: flex; align-items: center; justify-content: center;
  }
  .action-button svg { width: 34px; height: 34px; fill: var(--button-icon); }
  .action-price {
    font-weight: 600; font-size: 34px; line-height: 1;
    color: var(--button-icon);
  }

  /* App icon */
  .app-icon {
    position: absolute; left: 893px; top: 289px;
    width: 190px; height: 186px;
    border-radius: 34px;
    background: linear-gradient(180deg, #ffffff 0%, var(--icon-tile) 60%, var(--icon-tile-edge) 100%);
    box-shadow: 0 4px 10px rgba(0, 0, 0, 0.35);
  }
  .icon-emblem {
    position: absolute; left: 10px; top: 28px; width: 170px; height: 126px;
    border-radius: 50% 40% 40% 50% / 50%;
    background: radial-gradient(ellipse at 45% 50%, var(--fry-gold) 0%, var(--fry-deep) 78%, rgba(216, 102, 15, 0.2) 100%);
  }
  .app-name {
    position: absolute; left: 893px; width: 190px; top: 500px;
    text-align: center;
    font-weight: 400;
    font-size: 74px;
    line-height: 1;
    letter-spacing: 3px;
    color: var(--wordmark);
  }
</style>
</head>
<body>

  <section class="screen splash" aria-label="Splash screen">
    <div class="splash-photo" role="img" aria-label="Blurred close-up photo of fish and chips in warm orange tones"></div>
    <div class="splash-brand">
      <span class="splash-name">VELTO</span>
      <span class="splash-tagline">TO YOUR DOOR</span>
    </div>
  </section>

  <section class="screen main" aria-label="Main screen">
    <div class="main-header">
      <div class="header-emblem" role="img" aria-label="Brand emblem: golden fries inside a fish outline"></div>
    </div>
    <div class="main-photo" role="img" aria-label="Blurred photo of a plate of fish and chips"></div>
    <nav class="action-row">
      <div class="action-button" aria-label="Menu">
        <svg viewBox="0 0 34 34" aria-hidden="true">
          <rect x="7" y="5" width="20" height="24" rx="2"/>
          <rect x="11" y="5" width="2" height="24" fill="#bdbdbd"/>
        </svg>
      </div>
      <div class="action-button" aria-label="Prices">
        <span class="action-price">$</span>
      </div>
      <div class="action-button" aria-label="Order">
        <svg viewBox="0 0 34 34" aria-hidden="true">
          <ellipse cx="17" cy="15" rx="13" ry="10"/>
          <path d="M9 22 L6 30 L15 24 Z"/>
        </svg>
      </div>
    </nav>
  </section>

  <div class="app-icon" aria-label="App icon">
    <div class="icon-emblem" role="img" aria-label="Brand emblem: golden fries inside a fish outline"></div>
  </div>
  <p class="app-name">VELTO</p>

</body>
</html>
```